high-impact, conversion-focused website redesign for the government sector

Objective: To design and develop a high-impact, conversion-focused digital platform that solidifies Harrowgate Lumen Advisors (HLA) as the leading communications and strategy firm for government, defense, and industrial clients. The site must project authority, innovation, and sophisticated precision. See the creative breif for more information

Target Market(s)

Government contractors

Industry/Entity Type

Government, defense, industrials

Coding

Coded - Design and coding required

Number of Pages Required

5+ page

Font styles to use
Other font styles liked:
• See the current website

Requirements
Must have
• See design brief
Nice to have
• See design brief
Should not have
• See design brief

```html
<!DOCTYPE html>
<html lang="en">
<head>
<meta charset="utf-8">
<title>Harrowgate Lumen Advisors — Accelerate Your Mission</title>
<link rel="stylesheet" href="https://fonts.googleapis.com/css2?family=Black+Ops+One&family=Montserrat:wght@400;500;600;700&display=swap">
<style>
:root{
  --navy:#10304f;
  --navy-deep:#0b2540;
  --ink:#0f2a44;
  --text:#4a5563;
  --muted:#8a97a6;
  --paper:#ffffff;
  --mist:#f3f5f8;
  --line:#e3e7ec;
  --blue:#1f8ded;
  --green:#5db534;
  --stage:#ffffff;
}
*{box-sizing:border-box;margin:0;padding:0}
html,body{width:725px;height:1200px;overflow:hidden;background:var(--stage)}
body{position:relative;font-family:"Montserrat",sans-serif;color:var(--text)}
.page{position:absolute;left:276px;top:0;width:628px;height:4360px;transform:scale(0.2752);transform-origin:0 0;background:var(--paper);overflow:hidden}
.display{font-family:"Black Ops One",sans-serif;letter-spacing:1px;text-transform:uppercase}
.brand{display:flex;align-items:center;gap:5px;font-weight:700;font-size:9px;color:var(--ink);letter-spacing:.3px}
.brand .dot{width:9px;height:9px;border-radius:50%;background:var(--green)}
/* nav */
.site-nav{height:44px;display:flex;align-items:center;justify-content:space-between;padding:0 20px;font-size:7px;font-weight:700;color:var(--ink)}
.site-nav ul{display:flex;gap:14px;list-style:none}
.site-nav .active{color:var(--blue)}
/* hero */
.hero{height:246px;background:radial-gradient(ellipse at 60% 20%,#3a2e2a 0%,#1a1c22 45%,#0c0e12 100%);clip-path:polygon(0 0,100% 0,100% 100%,0 94%);text-align:center;color:#fff;padding-top:30px}
.hero h1{font-size:38px;line-height:60px;font-weight:400}
.hero p{width:420px;margin:22px auto 0;font-size:7.2px;line-height:14px;color:#dfe3e8}
/* intro */
.intro{position:relative;height:450px}
.intro .visual{position:absolute;left:30px;top:112px;width:262px;height:148px;background:linear-gradient(135deg,#0b1a33,#1d4b78 55%,#0a1424);box-shadow:0 4px 10px rgba(0,0,0,.25)}
.intro .copy{position:absolute;left:334px;top:80px;width:262px;font-size:6.6px;line-height:16px}
.intro .copy p+p{margin-top:18px}
.pledge{position:absolute;left:30px;top:334px;width:566px;height:96px;background:var(--mist);border-left:2px solid var(--blue);display:flex;align-items:center;justify-content:center;text-align:center;padding:0 44px;font-size:7.6px;line-height:18px;font-weight:600;color:var(--ink)}
/* results */
.results{height:960px;background:var(--navy);clip-path:polygon(0 0,100% 4%,100% 100%,0 100%);color:#fff;padding:118px 30px 0;margin-top:0}
.results h2{font-size:25px;text-align:center;font-weight:400}
.results .lead{display:flex;justify-content:space-between;align-items:flex-start;margin-top:34px}
.results .lead p{width:250px;font-size:7px;line-height:19px;color:#dbe3ec;margin-top:36px}
.results .lead .visual{width:262px;height:148px;background:linear-gradient(135deg,#0d1b2c,#2a5d86 50%,#101b28);box-shadow:0 4px 10px rgba(0,0,0,.35)}
.results h3{text-align:center;font-size:12px;font-weight:700;letter-spacing:1px;margin-top:56px}
.stats{display:flex;justify-content:center;margin-top:66px}
.stat{width:184px;text-align:center;padding:0 20px 28px}
.stat+.stat{border-left:1px solid rgba(255,255,255,.25)}
.stat strong{display:block;font-family:"Black Ops One",sans-serif;font-size:34px;font-weight:400}
.stat span{display:block;margin-top:16px;font-size:6px;line-height:13px;color:#c6d1dc}
.quote{position:relative;margin:90px auto 0;width:370px;text-align:center;font-size:6.4px;line-height:15px;color:#4f6a86}
.quote cite{display:block;margin-top:16px;font-style:normal}
.quote .arrow{position:absolute;top:56px;width:20px;height:20px;border:1px solid #4f6a86;border-radius:50%;display:flex;align-items:center;justify-content:center}
.quote .prev{left:-40px}.quote .next{right:-40px}
.dots{display:flex;justify-content:center;gap:5px;margin-top:12px}
.dots i{width:6px;height:6px;border-radius:50%;background:#4f6a86}
.dots i.on{background:#c6d1dc}
/* services */
.services{height:950px;background:var(--mist);text-align:center;padding-top:106px}
.services h2{font-size:25px;font-weight:400;color:var(--ink)}
.services .visual{width:466px;height:262px;margin:42px auto 0;background:linear-gradient(180deg,#0b1a2c,#1e5579 55%,#0a1522);box-shadow:0 4px 10px rgba(0,0,0,.25)}
.grid{display:grid;grid-template-columns:repeat(4,1fr);gap:2px;width:566px;margin:46px auto 0;background:var(--line)}
.cell{background:#fff;height:146px;display:flex;flex-direction:column;align-items:center;justify-content:center;gap:12px;font-size:8.6px;font-weight:700;line-height:12px;color:var(--ink)}
.cell svg{width:36px;height:36px;fill:none;stroke:var(--green);stroke-width:2;stroke-linecap:round;stroke-linejoin:round}
.btn{display:inline-block;background:var(--blue);color:#fff;font-size:7px;font-weight:700;letter-spacing:1px;padding:12px 32px;margin-top:42px}
/* edge */
.edge{height:350px;background:linear-gradient(180deg,#14304f,#1d4a72 50%,#143456);clip-path:polygon(0 4%,100% 0,100% 100%,0 100%);margin-top:-10px;text-align:center;color:#fff;padding-top:108px}
.edge h2{font-size:25px;font-weight:400}
.edge p{width:520px;margin:26px auto 0;font-size:6.6px;line-height:16px;color:#c7d3df}
.edge p+p{margin-top:24px}
/* expect */
.expect{position:relative;height:690px;padding-top:100px}
.expect h2{font-size:25px;line-height:46px;font-weight:400;color:var(--ink);text-align:center;width:560px;margin:0 auto}
.expect .copy{position:absolute;left:30px;top:250px;width:260px;font-size:6.2px;line-height:17px}
.expect .copy p+p{margin-top:16px}
.expect .visual{position:absolute;left:340px;top:324px;width:256px;height:144px;background:linear-gradient(135deg,#0c1820,#244a4c 50%,#0b141c);box-shadow:0 4px 10px rgba(0,0,0,.25)}
.expect .btn{position:absolute;left:244px;top:610px;margin:0;padding:11px 30px}
/* contact */
.contact{height:650px;background:var(--navy);clip-path:polygon(0 0,100% 3%,100% 100%,0 100%);color:#fff;text-align:center;padding-top:110px;position:relative}
.contact h2{font-size:25px;font-weight:400}
.contact .sub{font-size:6.6px;color:#c7d3df;margin-top:26px}
.form-slot{width:412px;height:136px;background:#fff;margin:36px auto 0;display:flex;align-items:center;justify-content:center;font-size:6.6px;color:var(--muted)}
.site-footer{position:absolute;left:40px;right:40px;top:510px;display:flex;justify-content:space-between;align-items:flex-start;font-size:6px;line-height:11px}
.site-footer .brand{color:#fff;margin-top:16px}
.site-footer ul{list-style:none;font-weight:700;line-height:21px;margin-left:60px}
.site-footer address{font-style:normal;color:#c7d3df;text-align:center;width:120px}
.site-footer address b{display:block;color:#fff;margin-bottom:6px}
</style>
</head>
<body>
<main class="page">
  <header class="site-nav">
    <ul><li>HOME</li><li>ADVISORY SERVICES</li><li>ABOUT US</li></ul>
    <div class="brand"><span class="dot"></span>HARROWGATE LUMEN ADVISORS</div>
    <ul><li class="active">BLOG</li><li>CONTACT US</li></ul>
  </header>

  <section class="hero" role="img" aria-label="Dark night-time view of the Earth from orbit behind the headline">
    <h1 class="display">Accelerate Your<br>Mission</h1>
    <p>Harrowgate Lumen Advisors exists for one reason to help connect the federal ecosystem with the technologies that matter most to America and her allies. We help build the communications, government affairs and marketing strategies and systems your organization needs to grow and protect market share –helping our clients meet their mission objectives.</p>
  </section>

  <section class="intro">
    <div class="visual" role="img" aria-label="Satellites orbiting above glowing holographic data screens"></div>
    <div class="copy">
      <p>Our team of award-winning communications strategists brings deep experience across government, defense, and technology. We build systems, teams, and campaigns that drive outcomes for federal contractors and innovators supporting national security, space, and industrial growth.</p>
      <p>Our team has served in the military, supported the DoD and federal leaders, and led communications, marketing, and government affairs for major government, tech and investment organizations. We understand the missions that matter — and we help our clients achieve them through precision communications, policy engagement, and strategic connection-building.</p>
    </div>
    <blockquote class="pledge">We are committed to strengthening the defense industrial base and enabling our clients to thrive through growth and transition to achieve mission success.</blockquote>
  </section>

  <section class="results">
    <h2 class="display">Proven Results That Drive Real Growth</h2>
    <div class="lead">
      <p>We've helped brands strengthen their digital presence, expand their network, and accelerate opportunities across the defense, space, and government sectors. In just one year, our clients have achieved:</p>
      <div class="visual" role="img" aria-label="Command centre console with glowing world map displays"></div>
    </div>
    <h3>BUSINESS GROWTH &amp; NETWORK EXPANSION</h3>
    <div class="stats">
      <div class="stat"><strong>+72%</strong><span>Increase in database contacts through CRM implementation and targeted marketing campaigns</span></div>
      <div class="stat"><strong>100+</strong><span>Introductions to tech-scouting contacts across the DoD and the aerospace &amp; defense ecosystem</span></div>
      <div class="stat"><strong>570%</strong><span>Positioned a client for transformative growth, fueling a 570% increase in stock price and attracting $50M AUD in new investment</span></div>
    </div>
    <div class="quote">
      <span class="arrow prev"><svg width="8" height="8" viewBox="0 0 8 8"><path d="M5 1 2 4l3 3" fill="none" stroke="#4f6a86"/></svg></span>
      <p>Partnering with this team has been one of the most valuable decisions we have made this year. Their strategic guidance opened doors across the defense community, sharpened how we present our mission, and connected us with leaders we could not reach on our own. They are responsive, organized and deeply trusted across the aerospace and defense ecosystem. All of this has created measurable impact and real value for our team.</p>
      <cite>–Dana Whitlock, Vice President of Customer Success, Summit Forge</cite>
      <span class="arrow next"><svg width="8" height="8" viewBox="0 0 8 8"><path d="M3 1l3 3-3 3" fill="none" stroke="#4f6a86"/></svg></span>
    </div>
    <div class="dots"><i></i><i class="on"></i><i class="on"></i></div>
  </section>

  <section class="services">
    <h2 class="display">Our Services</h2>
    <div class="visual" role="img" aria-label="Holographic Earth surrounded by futuristic control screens"></div>
    <div class="grid">
      <div class="cell"><svg viewBox="0 0 36 36"><circle cx="18" cy="18" r="4"/><circle cx="9" cy="9" r="4"/><circle cx="27" cy="9" r="4"/><circle cx="9" cy="27" r="4"/><circle cx="27" cy="27" r="4"/><path d="M12 12l3 3M24 12l-3 3M12 24l3-3M24 24l-3-3"/></svg>CORPORATE<br>COMMUNICATIONS</div>
      <div class="cell"><svg viewBox="0 0 36 36"><rect x="13" y="4" width="10" height="17" rx="5"/><path d="M8 17a10 10 0 0 0 20 0M18 27v5M13 32h10"/></svg>PUBLIC<br>RELATIONS</div>
      <div class="cell"><svg viewBox="0 0 36 36"><path d="M5 13 18 5l13 8zM7 13h22M9 16v11M14 16v11M22 16v11M27 16v11M5 30h26"/></svg>GOVERNMENT<br>AFFAIRS</div>
      <div class="cell"><svg viewBox="0 0 36 36"><path d="M18 5 32 30H4z"/><path d="M18 14v8M18 25v1"/></svg>CRISIS<br>COMMUNICATIONS</div>
      <div class="cell"><svg viewBox="0 0 36 36"><rect x="5" y="6" width="26" height="19" rx="2"/><path d="M9 20l6-6 4 3 7-7M13 31h10M18 25v6"/></svg>DIGITAL<br>MARKETING</div>
      <div class="cell"><svg viewBox="0 0 36 36"><circle cx="18" cy="18" r="4"/><circle cx="9" cy="9" r="4"/><circle cx="27" cy="9" r="4"/><circle cx="9" cy="27" r="4"/><circle cx="27" cy="27" r="4"/><path d="M12 12l3 3M24 12l-3 3M12 24l3-3M24 24l-3-3"/></svg>STRATEGIC<br>CONNECTIONS</div>
      <div class="cell"><svg viewBox="0 0 36 36"><path d="M5 5v26h26M10 27v-6M15 27v-9M20 27v-5M25 27v-11M9 16l7-7 5 5 9-8"/></svg>INVESTOR<br>RELATIONS</div>
      <div class="cell"><svg viewBox="0 0 36 36"><rect x="6" y="8" width="24" height="23" rx="2"/><path d="M6 14h24M12 5v6M24 5v6M11 19h2M17 19h2M23 19h2M11 25h2M17 25h2M23 25h2"/></svg>EVENT<br>MANAGEMENT</div>
    </div>
    <span class="btn">LEARN MORE</span>
  </section>

  <section class="edge" role="img" aria-label="Blue-toned operations room with data screens and robotic equipment">
    <h2 class="display">Our Edge</h2>
    <p>We combine deep federal sector insight, technical understanding, and a powerful network across government, industry, investors, and media. Our proven approach drives results — from major contract wins and successful M&amp;A to increased valuation, strategic investment, and political support.</p>
    <p>Our strategies begin with your mission and business goals, ensuring every message, relationship, and action advances growth and impact.</p>
  </section>

  <section class="expect">
    <h2 class="display">What To Expect When Partnering With Us</h2>
    <div class="copy">
      <p>With decades of experience, a results-focused methodology, and cutting-edge marketing and communications tools and technologies, we begin every engagement with a discovery and planning process to ensure we are building a strategy that cuts through the noise to achieve measurable results. As specialists in government and communications, we also review our client's current strategy for a strong and steady foundation.</p>
      <p>By fully understanding our client's goals, key milestones, potential areas of risk, ideal customer and investor targets, partner profiles, and other key drivers, we create messaging and strategy that goes beyond traditional brand awareness to meet mission objectives. As a full service firm, we work across all the areas in the graphic.</p>
      <p>Our time-tested methodology is based on building and executing a strategy aligned with client mission objectives. With the strategy in place, we execute tactics with precision, efficiency, and the highest quality of customer service.</p>
    </div>
    <div class="visual" role="img" aria-label="Glowing network lines over a dark global map display"></div>
    <span class="btn">GET IN TOUCH</span>
  </section>

  <section class="contact">
    <h2 class="display">Get In Touch</h2>
    <p class="sub">Ready to accelerate your mission? Let's discuss how we can help you achieve your goals.</p>
    <div class="form-slot">Contact form will be embedded here</div>
    <footer class="site-footer">
      <div class="brand"><span class="dot"></span>HARROWGATE LUMEN ADVISORS</div>
      <ul><li>HOME</li><li>ADVISORY SERVICES</li><li>ABOUT US</li><li>BLOG</li><li>CONTACT US</li></ul>
      <address><b>CONTACT US</b>info@harrowgatelumen.example<br><br>Summit Forge<br>Harrowgate Lumen Advisors<br>410 Ridge St, Suite 200<br>Corvale, TX 70000</address>
    </footer>
  </section>
</main>
</body>
</html>
```